KAZ Freightworks #ALLKAZ Business Cards & Letterhead

I am looking to business cards designed for our organization. We are currently undergoing a small re-branding that is taking place. Our organization is called KAZ Freightworks and we are headquartered in Phoenix, AZ. We primarily provide transportation and logistics services to the Meridel Parcel Bureau who is our largest customer. I would like to see a design that incorporates name, title, contact info, website, and address (this will be different depending on the employee). I would also like to see some color on the business card using our logo colors or a variation. I would like our logo on the back of the business card with the website displayed. The final design should communicate that we are a next generation transportation operate that focuses on being driver-first, customer-centric, innovative, and sustainable.We would also like our #ALLKAZ catch phrase incorporated as well.
Updates

Decision maker traveling outside of the country until Monday, November 25th.

Target Market(s)

Transportation & Logistics

Industry/Entity Type

Trucking Company

Contact Information for Business Card

-First and Last Name
-Position Title
-Contact Phone
-Contact Email
-Physical Address

Font styles to use
Serif

Colors

Designer to choose colors to be used in the design.

Requirements
Must have
• -KAZ logo prominently displayed
• -#ALLKAZ catch phrase used
• -Some amount of color, design gradient, etc.
• -Logo on the back with website listed (https://www.kazfreightco.example)

```html
<!DOCTYPE html>
<html lang="en">
<head>
<meta charset="utf-8">
<title>KAZ Freightworks Business Card</title>
<link href="https://fonts.googleapis.com/css2?family=Lora:wght@400;600&display=swap" rel="stylesheet">
<style>
  :root {
    --page-bg: #e9e6e1;
    --card-deep: #0c3137;
    --card-mid: #174a50;
    --card-light: #2c5d62;
    --brand-green: #6aad37;
    --name-green: #82b84a;
    --text-light: #d3dbd3;
    --wordmark: #dcdcd0;
  }
  html, body {
    margin: 0;
    padding: 0;
    width: 1200px;
    height: 1047px;
    overflow: hidden;
    background: var(--page-bg);
    font-family: "Lora", Georgia, serif;
  }
  .business-card {
    position: absolute;
    left: 100px;
    top: 251px;
    width: 1000px;
    height: 544px;
    border-radius: 24px;
    overflow: hidden;
    background: linear-gradient(100deg, var(--card-light) 0%, var(--card-mid) 35%, var(--card-deep) 70%);
    box-shadow: 0 12px 30px rgba(0,0,0,0.18);
  }
  .accent-band {
    position: absolute;
    top: 0;
    right: 0;
    width: 282px;
    height: 100%;
    background: linear-gradient(180deg, #77b840 0%, var(--brand-green) 100%);
  }
  .wordmark {
    position: absolute;
    left: 470px;
    top: 0;
    width: 488px;
    height: 544px;
    margin: 0;
    display: flex;
    align-items: center;
    justify-content: center;
    font-size: 150px;
    font-weight: 600;
    letter-spacing: 4px;
    color: var(--wordmark);
    line-height: 1;
  }
  .contact-block {
    position: absolute;
    left: 40px;
    top: 78px;
    color: var(--text-light);
  }
  .person-name {
    margin: 0;
    font-size: 36px;
    font-weight: 600;
    letter-spacing: 1px;
    color: var(--name-green);
    line-height: 1.1;
  }
  .person-title {
    margin: 4px 0 0;
    font-size: 23px;
    line-height: 1.3;
  }
  .address {
    margin: 38px 0 0;
    font-size: 24px;
    line-height: 32px;
    font-style: normal;
  }
  .contact-list {
    list-style: none;
    margin: 34px 0 0;
    padding: 0;
    font-size: 24px;
    line-height: 32px;
  }
  .contact-list li {
    display: flex;
    align-items: center;
    gap: 12px;
  }
  .contact-list svg {
    width: 16px;
    height: 16px;
    flex: none;
  }
  .catch-phrase {
    margin: 22px 0 0;
    font-size: 24px;
    font-weight: 600;
    letter-spacing: 2px;
    color: var(--name-green);
  }
</style>
</head>
<body>
  <section class="business-card">
    <div class="accent-band"></div>

    <p class="wordmark">KAZ</p>

    <div class="contact-block">
      <h1 class="person-name">DARREN HOLLOWAY</h1>
      <p class="person-title">Director</p>
      <address class="address">
        4120 North Cactus<br>
        Ridge Drive<br>
        Glendale, AZ 85306
      </address>
      <ul class="contact-list">
        <li>
          <svg viewBox="0 0 16 16" aria-hidden="true"><path d="M3 1.5l3 .5 1 3.5-2 1.2a9 9 0 0 0 4.3 4.3l1.2-2 3.5 1 .5 3-2 1.5C7 14 2 9 1.5 3.5z" fill="var(--brand-green)"/></svg>
          623-555-0148
        </li>
        <li>
          <svg viewBox="0 0 16 16" aria-hidden="true"><rect x="1.5" y="3.5" width="13" height="9" fill="none" stroke="var(--brand-green)" stroke-width="1.6"/><path d="M1.5 3.5l6.5 5 6.5-5" fill="none" stroke="var(--brand-green)" stroke-width="1.6"/></svg>
          info@kazfreightco.example
        </li>
        <li>
          <svg viewBox="0 0 16 16" aria-hidden="true"><circle cx="8" cy="8" r="6.5" fill="none" stroke="var(--brand-green)" stroke-width="1.5"/><path d="M1.5 8h13M8 1.5c-3 3.5-3 9.5 0 13M8 1.5c3 3.5 3 9.5 0 13" fill="none" stroke="var(--brand-green)" stroke-width="1.2"/></svg>
          www.kazfreightco.example
        </li>
      </ul>
      <p class="catch-phrase">#ALLKAZ</p>
    </div>
  </section>
</body>
</html>
```